Facial whitening product needs a packaging design

We need a packaging design for our new product named LUMIVOR Ultra-Bright Treatment. (btw Lumivor is our brand name). We want a package to look like a high end whitening treatment and eye-kicking. Here is the dimension for the labels and the dimensions the bottle for making a box is hight 5cm width 8 cm for the label (almost around the bottle) and 9.5 cm hight and 2.7 radius for a bottle (15ml) but we think we need a big box (the example is attached for the size and pattern of the box but not for the design) but the design is not fixed and all up to the designer.

Target Market(s)

Online shopper and mass targeted but the product need to look high end.

Industry/Entity Type

Product

Font styles to use
Sans Serif

Colors
34b8a4
ffffff

Requirements
Must have
• eye-kicking box that looks high end. I think white box would be great (file attached for example) and white bottle would be great but if you come with better idea then you can change it.
Nice to have
• You should look at Vitamin c box that a attached for an inspiration
• But the design is now free-style

```html
<!DOCTYPE html>
<html lang="en">
<head>
<meta charset="utf-8">
<title>LUMIVOR Ultra-Bright Treatment – Packaging Concepts</title>
<link href="https://fonts.googleapis.com/css2?family=Arimo:wght@400;700&family=Lato:wght@300;400;700&display=swap" rel="stylesheet">
<style>
  :root {
    --teal: #34b8a4;
    --teal-deep: #2aa596;
    --teal-pale: #dff1ee;
    --white: #ffffff;
    --ink: #333333;
    --ink-soft: #555555;
    --rule: #777777;
    --silver-light: #e6e6e6;
    --silver-dark: #b5b5b5;
    --stage-edge: #d5e6e7;
  }
  * { margin: 0; padding: 0; box-sizing: border-box; }
  html, body { width: 1200px; height: 1000px; overflow: hidden; }
  body {
    font-family: "Lato", sans-serif;
    background: radial-gradient(ellipse at 55% 45%, #ffffff 0%, #f1f7f7 55%, var(--stage-edge) 100%);
    position: relative;
    color: var(--ink);
  }
  .concept { position: absolute; overflow: hidden; background: var(--white); }
  .concept--a { left: 12px; top: 16px; width: 488px; height: 476px; }
  .concept--b { left: 12px; top: 506px; width: 488px; height: 478px;
    background: linear-gradient(180deg, var(--teal-deep) 0%, #6cc9bb 45%, #e4f3f1 100%); color: var(--white); }
  .concept--c { left: 648px; top: 16px; width: 489px; height: 477px; }
  .concept--d { left: 650px; top: 508px; width: 487px; height: 474px; }

  .concept-tag { position: absolute; font-size: 17px; font-weight: 300; color: var(--ink-soft); }

  .brand {
    position: absolute; font-weight: 300; font-size: 58px; letter-spacing: 3px;
    line-height: 1; white-space: nowrap;
  }
  .brand--center { left: 0; right: 0; text-align: center; }
  .product-name {
    position: absolute; font-size: 24px; line-height: 1; padding: 5px 0 6px;
    border-top: 1px solid var(--rule); border-bottom: 1px solid var(--rule);
    white-space: nowrap;
  }
  .product-name b { font-weight: 700; }
  .product-name span { font-weight: 400; }
  .product-type { position: absolute; font-size: 14px; letter-spacing: 3.5px; font-weight: 400; }

  .bottle {
    position: absolute; border-radius: 10px 10px 14px 14px;
    background: linear-gradient(90deg, #e4e4e4 0%, #ffffff 35%, #fafafa 65%, #d8d8d8 100%);
    box-shadow: 0 6px 10px rgba(0,0,0,0.08);
  }
  .bottle::after {
    content: ""; position: absolute; left: 0; right: 0; top: 62%; height: 7%;
    background: var(--teal); opacity: 0.9;
  }
  .flowers { position: absolute; }
  .flowers--mound {
    background: radial-gradient(ellipse at 50% 100%, #2fa896 0%, var(--teal) 45%, #5fc8b7 75%, rgba(95,200,183,0) 100%);
  }
  .flowers--strip { background: linear-gradient(180deg, #3fbca9, #6fcfc0); }
  .flowers--round { border-radius: 50%;
    background: radial-gradient(circle at 50% 50%, #2c9f8f 0%, var(--teal) 50%, #66c9b9 100%); }

  .claim-band {
    position: absolute; left: 0; width: 100%;
    background: linear-gradient(90deg, var(--silver-dark), var(--silver-light) 30%, #f2f2f2 50%, var(--silver-light) 70%, var(--silver-dark));
    color: var(--ink);
  }
  .claims {
    position: absolute; text-align: center; color: var(--ink);
    font-family: "Arimo", sans-serif; white-space: nowrap; line-height: 1.2;
  }
  .claims .tagline { font-size: 10.5px; padding-bottom: 3px; border-bottom: 1px solid var(--rule); }
  .claims .benefit { font-size: 10.5px; padding: 3px 0 3px; border-bottom: 1px solid var(--rule); }
</style>
</head>
<body>

  <section class="concept concept--a">
    <div class="brand brand--center" style="top:28px;">LUMIVOR</div>
    <div class="product-name" style="left:136px; width:218px; top:97px; text-align:center;"><b>ULTRA</b><span>-BRIGHT</span></div>
    <div class="product-type" style="left:0; right:0; top:139px; text-align:center;">TREATMENT</div>
    <div class="flowers flowers--mound" role="img" aria-label="Teal dahlia blooms clustered behind the bottle" style="left:-20px; width:528px; top:270px; height:140px;"></div>
    <div class="bottle" role="img" aria-label="White pump bottle of Ultra-Bright Treatment" style="left:213px; top:162px; width:65px; height:238px;"></div>
    <div class="claim-band" style="top:408px; height:42px;">
      <div class="claims" style="left:136px; width:218px; top:5px;">
        <div class="tagline">for a brighter, more radiant complexion</div>
        <div class="benefit">LIGHTEN SKIN TONE &amp; REDUCE DARK SPOTS</div>
      </div>
    </div>
    <div class="flowers flowers--strip" role="img" aria-label="Teal dahlia petals" style="left:0; width:100%; top:450px; height:26px;"></div>
  </section>
  <div class="concept-tag" style="left:512px; top:430px;">A</div>

  <section class="concept concept--b">
    <div class="brand brand--center" style="top:28px;">LUMIVOR</div>
    <div class="product-name" style="left:136px; width:218px; top:98px; text-align:center; border-color:var(--white);"><b>ULTRA</b><span>-BRIGHT</span></div>
    <div class="product-type" style="left:0; right:0; top:141px; text-align:center;">TREATMENT</div>
    <div class="flowers flowers--mound" role="img" aria-label="Teal dahlia blooms clustered behind the bottle" style="left:-20px; width:528px; top:274px; height:136px;"></div>
    <div class="bottle" role="img" aria-label="White pump bottle of Ultra-Bright Treatment" style="left:213px; top:166px; width:65px; height:238px;"></div>
    <div class="claim-band" style="top:406px; height:43px;">
      <div class="claims" style="left:128px; width:226px; top:5px;">
        <div class="tagline">for a brighter, more radiant complexion</div>
        <div class="benefit">LIGHTEN SKIN TONE &amp; REDUCE DARK SPOTS</div>
      </div>
    </div>
    <div class="flowers flowers--strip" role="img" aria-label="Teal dahlia petals" style="left:0; width:100%; top:449px; height:29px;"></div>
  </section>
  <div class="concept-tag" style="left:510px; top:928px;">B</div>

  <section class="concept concept--c">
    <div class="brand brand--center" style="top:28px;">LUMIVOR</div>
    <div class="product-name" style="left:134px; width:200px; top:97px; text-align:center; color:var(--teal); border-color:var(--teal);"><b>ULTRA</b><span>-BRIGHT</span></div>
    <div class="product-type" style="left:0; right:0; top:139px; text-align:center;">TREATMENT</div>
    <div class="flowers flowers--round" role="img" aria-label="Single teal dahlia on a long stem" style="left:24px; top:205px; width:250px; height:230px;"></div>
    <div class="flowers" style="left:146px; top:420px; width:4px; height:57px; background:var(--teal);" aria-hidden="true"></div>
    <div class="bottle" role="img" aria-label="White pump bottle of Ultra-Bright Treatment" style="left:322px; top:176px; width:68px; height:232px;"></div>
    <div class="claims" style="left:240px; width:227px; top:419px;">
      <div class="tagline">for a brighter, more radiant complexion</div>
      <div class="benefit">LIGHTEN SKIN TONE &amp; REDUCE DARK SPOTS</div>
    </div>
  </section>
  <div class="concept-tag" style="left:1154px; top:445px;">C</div>

  <section class="concept concept--d">
    <div class="brand" style="left:18px; top:28px;">LUMIVOR</div>
    <div class="product-name" style="left:20px; width:227px; top:98px; padding-left:2px;"><b>ULTRA</b><span>-BRIGHT</span></div>
    <div class="product-type" style="left:20px; top:139px;">TREATMENT</div>
    <div class="flowers flowers--round" role="img" aria-label="Small round teal dahlia bloom" style="left:40px; top:219px; width:124px; height:124px;"></div>
    <div class="flowers flowers--round" role="img" aria-label="Large teal dahlia bloom cropped at the edge" style="left:392px; top:122px; width:320px; height:320px;"></div>
    <div class="bottle" role="img" aria-label="White pump bottle of Ultra-Bright Treatment" style="left:280px; top:175px; width:65px; height:232px;"></div>
    <div class="claims" style="left:20px; width:227px; top:423px; text-align:left;">
      <div class="tagline">for a brighter, more radiant complexion</div>
      <div class="benefit">LIGHTEN SKIN TONE &amp; REDUCE DARK SPOTS</div>
    </div>
  </section>
  <div class="concept-tag" style="left:1150px; top:942px;">D</div>

</body>
</html>
```